依頼詳細
・B5縦カラー(裏面1c)
・出演アーティストは2組(1.森田ユミ&ルアペドラ、2.吉川沙織&前園剛)で1.がメインアーティストです。
・写真は適宜切り抜きなどしてご使用ください。
・ルアペドラ全員写真+青木カナ1人(写真1,2 いずれか)+ロゴ(適宜着色など)+吉川沙織&前園剛をレイアウトお願いします。

納品時にはSNSなどに使用するバナー画像作成もあわせてお願いいたします。
・コンペでは表面デザインとバナー(横 16:9 )のみお願いします。
決定後裏面に記載する詳細情報をお知らせして仕上げていただきたいと思います。
・バナー画像には詳細テキスト情報は原則として不要です
記載項目
【タイトル】凍てつく宵のフェスタ
【日付】2022年12月16日(金)
【会場名】代官山 ゆうべの窓に灯ともして
渋谷区代官山町14-7
ルミエール代官山B1
【出演者名】
・森田ユミ&ルア・ペドラ
(森田ユミ vocal、杉本健二 sax、大塚理恵 cl、沢井隆史 sax、今野英樹 sax、柳田さえ perc、西川昭夫 bass、川端修平 drums、野口康弘 guitar)
・吉川沙織 vocal & 前園剛 8st-guitar

【時間、料金】
開場 18:30
開演 19:30
前売4000円
当日4500円
(共に+1ドリンク代600円)
サイズ
B5
ページ数
両面
希望イメージ
シンプル 複雑
単色 カラフル
暗い 明るい
日常 高級
遊び心 厳粛
未来的 伝統的
女性的 男性的
希望する色
ライブタイトル、内容にふさわしい色をご提案いただければ幸いです。
納品ファイル
• 高解像度JPG (.jpg)
• イラストレーター形式 (.ai)
• PNG形式 (.png)
補足説明
ルア・ペドラ
ブラジル在住歴22年の森田ユミが日本に帰国後、ブラジルで培ってきた4本サックスがあるラテンコンボを日本で再結成したいと思い出来たのがこのルア・ペドラです。森田ユミのオリジナル曲を中心に、ラテンチックなサウンドにとことん楽しさを追求するコンセプトです。特にライブの後半にはブラジル北東部のカーニバル体験が出来て、思わず心と体が踊り出すことでしょう。

季節感とイベント内容に即したデザインでアーティストにも気に入ってもらえました。

この度は多くのご提案をいただきありがとうございました。
いいデザインが沢山あり絞るのが大変でした。
当選とできなかった皆様にはまた別の機会にお願い出来ればと思っております。
ありがとうございました。

```html
<!DOCTYPE html>
<html lang="ja">
<head>
<meta charset="utf-8">
<title>凍てつく宵のフェスタ</title>
<link href="https://fonts.googleapis.com/css2?family=Dela+Gothic+One&family=Noto+Sans+JP:wght@400;700;900&family=Montserrat:wght@600;700;800&display=swap" rel="stylesheet">
<style>
  :root {
    --navy: #1f2d6e;
    --green: #0b8c3c;
    --yellow: #f3c300;
    --ink: #1b1b1b;
    --paper: #ffffff;
  }
  * { margin: 0; padding: 0; box-sizing: border-box; }
  html, body { width: 848px; height: 1200px; overflow: hidden; background: var(--paper); }
  .flyer {
    position: relative; width: 848px; height: 1200px; overflow: hidden;
    background: var(--paper); color: var(--ink);
    font-family: "Noto Sans JP", sans-serif;
  }
  .tagline {
    position: absolute; right: 90px; top: 50px; text-align: right;
    font-weight: 700; font-size: 24px; line-height: 1.45; letter-spacing: 0.08em; color: var(--ink);
  }
  .title { position: absolute; left: 0; top: 135px; width: 848px; font-family: "Dela Gothic One", sans-serif; font-weight: 400; }
  .title-line { position: absolute; white-space: nowrap; line-height: 1; }
  .title-line--first { left: 92px; top: 0; font-size: 158px; letter-spacing: -0.02em; }
  .title-line--second { left: 80px; top: 205px; font-size: 120px; letter-spacing: -0.02em; }
  .title .small { font-size: 0.62em; vertical-align: 0.1em; }
  .c-navy { color: var(--navy); }
  .c-green { color: var(--green); }
  .c-yellow { color: var(--yellow); }
  .note { position: absolute; font-size: 44px; color: var(--navy); line-height: 1; }
  .flag { position: absolute; left: 742px; top: 235px; }

  .section-label {
    position: absolute; font-family: "Montserrat", sans-serif; font-weight: 700;
    font-size: 22px; color: var(--green); letter-spacing: 0.04em;
  }
  .performer {
    position: absolute; font-weight: 900; font-size: 25px; line-height: 1.4; color: var(--navy);
  }
  .act-label { left: 92px; top: 650px; }
  .act-name { left: 92px; top: 680px; }
  .band-photo { position: absolute; left: 240px; top: 640px; width: 420px; height: 180px;
    background: linear-gradient(180deg, #8d8476 0%, #5e5549 100%); }
  .lead-photo { position: absolute; left: 620px; top: 585px; width: 215px; height: 265px;
    background: linear-gradient(160deg, #d9cfc8 0%, #4a3b38 100%); }
  .band-name {
    position: absolute; left: 470px; top: 735px; display: flex; align-items: center; gap: 8px;
    background: var(--paper); padding: 10px 14px; border-radius: 50px;
    font-weight: 900; font-size: 20px; color: var(--navy);
  }
  .band-name .dot { width: 14px; height: 14px; border-radius: 50%; background: var(--yellow); }

  .guest-label { left: 92px; top: 910px; }
  .guest-name { left: 92px; top: 940px; }
  .guest-photo-vocal { position: absolute; left: 540px; top: 880px; width: 150px; height: 160px;
    background: linear-gradient(180deg, #e8e6e2 0%, #9a928a 100%); }
  .guest-photo-guitar { position: absolute; left: 700px; top: 880px; width: 135px; height: 160px;
    background: linear-gradient(180deg, #c7c2bb 0%, #5b4a3c 100%); }

  .date {
    position: absolute; left: 28px; top: 1055px; font-family: "Montserrat", sans-serif;
    font-weight: 800; font-size: 62px; color: var(--navy); letter-spacing: 0.01em; line-height: 1;
  }
  .date .dow { font-size: 34px; margin-left: 8px; }
  .info { position: absolute; left: 28px; top: 1128px; font-size: 15px; font-weight: 700; line-height: 1.75; color: var(--ink); }
  .info .key { font-family: "Montserrat", sans-serif; font-size: 12px; color: var(--paper);
    background: var(--navy); padding: 0 4px; margin-right: 4px; }
  .info .price { margin-left: 10px; }
  .info .small { font-size: 12px; }
</style>
</head>
<body>
<main class="flyer">
  <p class="tagline">本格的なブラジル音楽で<br>一夜のカーニバルを</p>

  <h1 class="title">
    <span class="title-line title-line--first"><span class="c-navy">凍</span><span class="c-green">て</span><span class="c-yellow">つ</span><span class="c-navy">く</span></span>
    <span class="title-line title-line--second"><span class="c-green">宵</span><span class="small c-navy">の</span><span class="c-yellow">フ</span><span class="c-navy">ェ</span><span class="c-green">ス</span><span class="c-yellow">タ</span></span>
  </h1>
  <span class="note" style="left:40px;top:160px;">♪</span>
  <span class="note" style="left:748px;top:165px;">♫</span>
  <span class="note" style="left:36px;top:370px;">♪</span>
  <span class="note" style="left:780px;top:380px;">♪</span>
  <svg class="flag" width="72" height="50" viewBox="0 0 72 50" aria-hidden="true">
    <rect width="72" height="50" fill="var(--green)"/>
    <polygon points="36,6 66,25 36,44 6,25" fill="var(--yellow)"/>
    <circle cx="36" cy="25" r="11" fill="var(--navy)"/>
  </svg>

  <span class="section-label act-label">act</span>
  <p class="performer act-name">森田ユミ &amp;<br>ルア・ペドラ</p>
  <div class="band-photo" role="img" aria-label="ルア・ペドラのメンバー集合写真"></div>
  <div class="lead-photo" role="img" aria-label="森田ユミのポートレート写真"></div>
  <div class="band-name"><span class="dot"></span>ルア・ペドラ</div>

  <span class="section-label guest-label">guest</span>
  <p class="performer guest-name">吉川沙織 &amp; 前園剛</p>
  <div class="guest-photo-vocal" role="img" aria-label="吉川沙織のポートレート写真"></div>
  <div class="guest-photo-guitar" role="img" aria-label="ギターを持つ前園剛の写真"></div>

  <p class="date">2022.12.16<span class="dow">FRI</span></p>
  <p class="info">
    <span class="key">open</span>18:30 <span class="key">start</span>19:30<br>
    <span class="key">venue</span>代官山 ゆうべの窓に灯ともして
    <span class="price"><span class="key">adv</span>¥4,000</span>
    <span class="price"><span class="key">door</span>¥4,500</span> <span class="small">(+1drink)</span>
  </p>
</main>
</body>
</html>
```